Dental Business Card

I need Dental oriented business cards.
On the front side -
- on the first line, my name:
Dr Marlo Vintner
- on the second line (just underneath):
Doctor of Dental Medicine
- on the third line, or underneath that or in a corner, I would like the address and phone number:
5182 Ch. Birchfield
Montreal QC H2T 4B9
514-629-5074
- other than that i would maybe like a logo of a tooth, but i want it to be subtle and very basic!
- I would like the card to be preferably black or dark grey-ish with the writing in white
On the other side -
- 2-3 lines with the possibility to write the next appointment the box with the lines should be white, with the rest of the card being black

```html
<!DOCTYPE html>
<html lang="en">
<head>
<meta charset="utf-8">
<title>Dental Business Card – Dr Marlo Vintner</title>
<link href="https://fonts.googleapis.com/css2?family=Lato:wght@400;700&display=swap" rel="stylesheet">
<style>
  :root {
    --backdrop: #2b2b2b;
    --card-dark: #1f1f20;
    --card-darker: #171718;
    --ink-light: #ffffff;
    --ink-soft: #d6d6d6;
    --rule: #5a5a5a;
    --slip-white: #f4f4f4;
    --slip-pattern: #e2e2e2;
    --pattern-tone: #2c2c2d;
  }
  * { box-sizing: border-box; margin: 0; padding: 0; }
  html, body {
    width: 1200px; height: 1108px; overflow: hidden;
    background: var(--backdrop);
    font-family: "Lato", sans-serif;
  }
  .card-set {
    position: relative; width: 1200px; height: 1108px;
  }
  .card {
    position: absolute; top: 239px;
    width: 400px; height: 630px;
    border-radius: 22px; overflow: hidden;
    background: var(--card-dark);
    box-shadow: 0 14px 30px rgba(0,0,0,0.45);
  }
  .card--front { left: 170px; }
  .card--back { left: 630px; }

  /* Front */
  .practice-mark {
    position: absolute; top: 120px; left: 0; width: 100%;
    display: flex; align-items: center; justify-content: center; gap: 14px;
    color: var(--ink-light); font-weight: 700; font-size: 30px; letter-spacing: 1px;
  }
  .practice-mark__dot {
    width: 18px; height: 18px; border-radius: 50%; background: var(--ink-light);
  }
  .identity {
    position: absolute; top: 352px; left: 0; width: 100%;
    text-align: center; color: var(--ink-light);
  }
  .identity__name {
    font-weight: 700; font-size: 29px; text-transform: uppercase; letter-spacing: 0.3px;
  }
  .identity__title {
    font-size: 18px; color: var(--ink-soft); margin-top: 2px;
  }
  .identity__rule {
    width: 170px; height: 1px; background: var(--rule); margin: 14px auto;
  }
  .identity__phone { font-size: 20px; }
  .identity__address { font-size: 19px; line-height: 1.3; }

  /* Back */
  .back__pattern {
    position: absolute; inset: 0 0 auto 0; height: 400px;
    background: linear-gradient(180deg, var(--pattern-tone), var(--card-darker));
  }
  .back__heading {
    position: absolute; top: 400px; left: 0; width: 100%; height: 60px;
    background: var(--card-darker);
    color: var(--ink-light); font-weight: 700; font-size: 25px;
    text-align: center; line-height: 60px; letter-spacing: 0.5px;
  }
  .back__slip {
    position: absolute; top: 460px; left: 0; width: 100%; bottom: 0;
    background: linear-gradient(180deg, var(--slip-white), var(--slip-pattern));
  }
</style>
</head>
<body>
  <main class="card-set">
    <section class="card card--front" aria-label="Business card front">
      <div class="practice-mark">
        <span class="practice-mark__dot"></span>
        <span class="practice-mark__name">Vintner Dental</span>
      </div>
      <div class="identity">
        <h1 class="identity__name">Dr Marlo Vintner</h1>
        <p class="identity__title">Doctor of Dental Medicine</p>
        <div class="identity__rule"></div>
        <p class="identity__phone">514-629-5074</p>
        <div class="identity__rule"></div>
        <p class="identity__address">5182 Ch. Birchfield<br>Montreal QC H2T 4B9</p>
      </div>
    </section>

    <section class="card card--back" aria-label="Business card back">
      <div class="back__pattern" role="img" aria-label="Subtle repeating tooth motif pattern in dark grey"></div>
      <h2 class="back__heading">NEXT APPOINTMENT</h2>
      <div class="back__slip" role="img" aria-label="White appointment area with faint light grey tooth motif pattern"></div>
    </section>
  </main>
</body>
</html>
```